I've recently started my own party promotion business. We are currently based in Sydney, Australia. Thus, most of our events are based in the Sydney Metropolitan area, with an eye to continue expanding our business and promote parties right through the Asia Pacific region.

Company details are as follows;

*Company name - Bostrane Promotions
*Company motto - The Velvet Night Hosts
*Website - www.bostrane-example.com
*Phone number - 0455 026 374
*Employee Name - Mick Orandy
*Employee Title - Executive Chief of Operations - Asia Pacific

We need the following items/templates designed;

1. Business Cards
2. Letterhead
3. Envelopes
4. Envelope seals/stickers

At the moment, I am using my mobile number as the main point of contact, for any enquiries. Thus I don't have a landline or fax number. I don't have my 'www.bostrane-example.com' website up and running yet either. Therefore, I would like the templates/designs provided to allow me to add those details at a later date, with ease.

1. Business card.
Note: Please be aware that the design provided will also act as a template to use for any future employees I take on board. Therefore I need to be able to edit the name, title and mobile number with ease.
A. Front Side. I would like my logo to be on the left with the company name to the right of the logo, along the top of the business card. With our company motto directly underneath. Then my name, title, mobile phone number and website following beneath.
B. On the reverse side of the card, I would like the full logo to be centred, with the motto underneath. I want both sides to be royal purple, with everything in glittering gold, consistent with my logo.

2. Letterhead.
A. I would like the full logo to be based to the top right hand corner. With the company motto following underneath.
B. Followed by three lines/spaces to add an address, phone number and fax number, when it becomes applicable. I want these details to be in gold without the purple background. Remembering I need to be able to edit these details when they become available.
C. I would like the website to be emblazoned in gold along the bottom, with the logo on each side of the website address. I also want these details to be in gold without the purple background.

3. Envelopes
Please use your creative expression for this particular template, so as long as it has a consistent matching feel with the Letterhead.

4. Envelope Seals/Stickers
Again, feel free to use your creative flair, so long as it's consistent with the other items. However, I would like these to be round. With only the logo included on the purple background.

If there are any questions, please call me on my mobile number. 0455 026 374.

Many thanks.

Mick

```html
<!DOCTYPE html>
<html lang="en">
<head>
<meta charset="utf-8">
<title>Bostrane Promotions – Stationery Set</title>
<link rel="stylesheet" href="https://fonts.googleapis.com/css2?family=Source+Sans+3:wght@300;400;600&display=swap">
<style>
  :root {
    --purple: #4f1668;
    --gold: #b8960b;
    --gold-soft: #c9a227;
    --gold-label: #a88a12;
    --faint: #f6f2e1;
    --ink: #333333;
    --line: #b9b9b9;
    --paper: #ffffff;
  }
  * { box-sizing: border-box; margin: 0; padding: 0; }
  html, body {
    width: 1200px; height: 800px; overflow: hidden;
    background: var(--paper);
    font-family: "Source Sans 3", Arial, sans-serif;
    color: var(--ink);
  }
  .board { position: relative; width: 1200px; height: 800px; }
  .abs { position: absolute; }

  .caption { position: absolute; font-size: 8.5px; color: #555; white-space: nowrap; }
  .caption.center { transform: translateX(-50%); text-align: center; }

  .sheet { position: absolute; background: var(--paper); border: 1px solid var(--line); overflow: hidden; }

  .mark {
    position: absolute; display: flex; flex-direction: column; align-items: center;
    transform: translateX(-50%);
  }
  .mark-dot { border-radius: 50%; background: var(--gold-soft); }
  .mark-name {
    font-weight: 400; color: var(--gold); text-transform: uppercase;
    letter-spacing: 1.5px; text-align: center; white-space: nowrap; line-height: 1.1;
  }
  .motto { color: var(--gold); font-size: 8px; white-space: nowrap; }

  .fields { position: absolute; text-align: right; color: var(--gold-label); font-size: 8.5px; }
  .fields span { position: absolute; right: 0; white-space: nowrap; }

  .footer-band { position: absolute; left: 0; right: 0; height: 9px; }
  .footer-band .bar { position: absolute; top: 0; height: 9px; background: var(--gold); }
  .footer-band .url {
    position: absolute; top: -3px; color: var(--gold); font-size: 11px;
    letter-spacing: 2px; white-space: nowrap; transform: translateX(-50%);
  }

  .watermark { position: absolute; border-radius: 50%; background: var(--faint);
    display: flex; align-items: center; justify-content: center; }
  .watermark span { color: #efe9cf; font-weight: 400; text-transform: uppercase;
    letter-spacing: 3px; white-space: nowrap; }

  .card { position: absolute; width: 242px; height: 142px; overflow: hidden; }
  .card.front { background: var(--paper); border: 1px solid var(--line); }
  .card.back { background: var(--purple); }
  .card .panel { position: absolute; left: 0; top: 0; width: 97px; height: 70px; background: var(--purple); }
  .card .text-right { position: absolute; right: 16px; text-align: right; white-space: nowrap; }
  .brand-line { font-size: 9.5px; color: var(--purple); }
  .brand-line b { font-weight: 600; }
  .small { font-size: 6.5px; color: var(--ink); }
  .person { font-size: 9.5px; color: var(--purple); font-weight: 400; }
  .tab { position: absolute; right: 0; top: 63px; width: 10px; height: 21px; background: var(--purple); }
  .detail { font-size: 8px; color: var(--ink); }

  .seal { position: absolute; width: 100px; height: 100px; border-radius: 50%; background: var(--purple);
    display: flex; align-items: center; justify-content: center; }
  .seal span { font-size: 8px; letter-spacing: 1px; text-transform: uppercase; text-align: center; line-height: 1.3; }
  .seal.gold span { color: var(--gold-soft); }
  .seal.white span { color: #ffffff; }
</style>
</head>
<body>
<main class="board">

  <!-- Letterhead -->
  <section class="sheet letterhead" style="left:18px; top:10px; width:552px; height:780px;">
    <div class="watermark" role="img" aria-label="Faint large brand emblem backdrop" style="left:53px; top:250px; width:440px; height:440px;">
      <span style="font-size:26px;">Bostrane Promotions</span>
    </div>
    <div class="mark" style="left:477px; top:26px;">
      <div class="mark-dot" style="width:52px; height:52px;"></div>
      <div class="mark-name" style="font-size:13px; margin-top:14px; width:110px; white-space:normal;">Bostrane Promotions</div>
    </div>
    <div class="motto abs" style="left:477px; top:127px; transform:translateX(-50%);">The Velvet Night Hosts</div>
    <div class="fields" style="left:0; top:0; width:431px; height:230px;">
      <span style="top:151px;">Address :</span>
      <span style="top:188px;">Phone :</span>
      <span style="top:206px;">Fax :</span>
    </div>
    <div class="footer-band" style="top:746px;">
      <div class="bar" style="left:0; width:177px;"></div>
      <div class="url" style="left:271px; font-size:10px; letter-spacing:1.2px;">www.bostrane-example.com</div>
      <div class="bar" style="left:362px; right:0;"></div>
    </div>
  </section>

  <p class="caption" style="left:582px; top:14px;">Letterhead</p>
  <p class="caption" style="left:582px; top:33px;">Size (210x297 mm)</p>

  <!-- Business card front -->
  <article class="card front" style="left:648px; top:71px;">
    <div class="panel">
      <div class="mark" style="left:48px; top:10px;">
        <div class="mark-dot" style="width:26px; height:26px;"></div>
        <div class="mark-name" style="font-size:6px; margin-top:5px; color:var(--gold-soft);">Bostrane Promotions</div>
      </div>
    </div>
    <div class="text-right brand-line" style="top:15px;"><b>BOSTRANE</b> PROMOTIONS</div>
    <div class="text-right small" style="top:32px;">The Velvet Night Hosts</div>
    <div class="text-right person" style="top:63px;">MICK ORANDY</div>
    <div class="tab"></div>
    <div class="text-right small" style="top:77px; font-size:5.5px;">Executive Chief of Operations - Asia Pacific</div>
    <div class="text-right detail" style="top:97px;">Tel.: 0455 026 374</div>
    <div class="text-right detail" style="top:116px;">www.bostrane-example.com</div>
  </article>
  <p class="caption center" style="left:767px; top:224px;">Business Card &nbsp;/&nbsp; Size (92x54 mm) &nbsp;/ Front</p>

  <!-- Business card back -->
  <article class="card back" style="left:648px; top:260px;">
    <div class="mark" style="left:121px; top:18px;">
      <div class="mark-dot" style="width:44px; height:44px;"></div>
      <div class="mark-name" style="font-size:12px; margin-top:22px; color:var(--gold-soft);">Bostrane Promotions</div>
    </div>
    <div class="motto abs" style="left:121px; top:117px; transform:translateX(-50%); color:var(--gold-soft);">The Velvet Night Hosts</div>
  </article>
  <p class="caption center" style="left:767px; top:414px;">Business Card &nbsp;/&nbsp; Size (92x54 mm) &nbsp;/ Back</p>

  <!-- Seals -->
  <div class="seal gold" style="left:995px; top:72px;"><span>Bostrane<br>Promotions</span></div>
  <p class="caption center" style="left:1045px; top:193px;">Seal &nbsp;/&nbsp; Size (38 mm diameter)</p>

  <div class="seal white" style="left:995px; top:252px;"><span>Bostrane<br>Promotions</span></div>
  <p class="caption center" style="left:1045px; top:373px;">Option 2</p>
  <p class="caption center" style="left:1045px; top:391px;">Seal &nbsp;/&nbsp; Size (38 mm diameter)</p>

  <!-- Envelope -->
  <p class="caption" style="left:585px; top:451px;">Envelop</p>
  <p class="caption" style="left:585px; top:470px;">Size (227 x 115 mm)</p>

  <section class="sheet envelope" style="left:585px; top:489px; width:601px; height:301px;">
    <div class="watermark" role="img" aria-label="Faint brand emblem backdrop" style="left:50px; top:20px; width:220px; height:220px;">
      <span style="font-size:13px; letter-spacing:2px;">Bostrane Promotions</span>
    </div>
    <div class="mark" style="left:527px; top:24px;">
      <div class="mark-dot" style="width:50px; height:50px;"></div>
      <div class="mark-name" style="font-size:12px; margin-top:12px; width:100px; white-space:normal;">Bostrane Promotions</div>
    </div>
    <div class="motto abs" style="left:527px; top:126px; transform:translateX(-50%); color:var(--ink); font-size:7.5px;">The Velvet Night Hosts</div>
    <div class="fields" style="left:0; top:0; width:464px; height:230px; font-size:9.5px;">
      <span style="top:157px;">Address :</span>
      <span style="top:194px;">Phone :</span>
      <span style="top:212px;">Fax :</span>
    </div>
    <div class="footer-band" style="top:267px;">
      <div class="bar" style="left:0; width:70px;"></div>
      <div class="url" style="left:159px; font-size:10px; letter-spacing:1.2px;">www.bostrane-example.com</div>
      <div class="bar" style="left:248px; right:0;"></div>
    </div>
  </section>

</main>
</body>
</html>
```